I would love for my business card to be fun and sophisicated. The clients are people that could afford nice well crafted wigs. These wigs are not like granny wigs. The're for women who are stylish and what to look there best especially if they are dealing with cancer are some from of hair loss. Do not want the card to appear crowded with to much information. If I need to eliminate some data, let me know.
Thanks

Industry/Entity Type

Hair

Contact Information for Business Card

L Radiant Tresses, Marianne Holt, owner, stylist

Wigs/Studio Showroom
Extensions
Hair Replacement
Private Room

24618 Crest Meadow Loop, Suite. R
Irvine, CA 90377
(949) 582-7041
Email: wigs@lradianttresses-example.com
www.lradianttresses-example.com

```html
<!DOCTYPE html>
<html lang="en">
<head>
<meta charset="utf-8">
<title>L Radiant Tresses – Business Card</title>
<link rel="stylesheet" href="https://fonts.googleapis.com/css2?family=Open+Sans:wght@400;600&display=swap">
<style>
  :root {
    --backdrop: #e4e4e6;
    --photo-light: #ecebe8;
    --photo-hair: #5a3424;
    --photo-skin: #d9b49a;
    --panel: #463e40;
    --panel-deep: #3b3436;
    --divider: rgba(255, 255, 255, 0.09);
    --divider-dark: rgba(0, 0, 0, 0.25);
    --text-light: #f4f1f1;
    --text-muted: #d9d3d4;
    --brand-red: #d42a2e;
    --icon-phone: #8cc63f;
    --icon-mail: #e0504a;
    --icon-pin: #3aa7d1;
  }
  * { box-sizing: border-box; margin: 0; padding: 0; }
  html, body {
    width: 1200px;
    height: 740px;
    overflow: hidden;
    background: var(--backdrop);
    font-family: "Open Sans", Arial, sans-serif;
  }
  .canvas {
    width: 1200px;
    height: 740px;
    display: flex;
    align-items: center;
    justify-content: center;
  }
  .business-card {
    width: 370px;
    height: 648px;
    background: var(--panel);
    display: flex;
    flex-direction: column;
    overflow: hidden;
    box-shadow: 0 10px 30px rgba(0, 0, 0, 0.18);
  }
  .portrait {
    position: relative;
    height: 290px;
    background:
      radial-gradient(ellipse 30% 38% at 62% 40%, var(--photo-skin) 0%, rgba(217,180,154,0) 100%),
      radial-gradient(ellipse 48% 55% at 58% 30%, var(--photo-hair) 0%, rgba(90,52,36,0.55) 60%, rgba(90,52,36,0) 100%),
      linear-gradient(180deg, #e9e7e3 0%, var(--photo-light) 100%);
  }
  .brand-name {
    position: absolute;
    left: 24px;
    bottom: 26px;
    font-size: 25px;
    font-weight: 600;
    color: var(--brand-red);
    letter-spacing: 0.2px;
  }
  .panel {
    flex: 1;
    background: linear-gradient(180deg, var(--panel) 0%, var(--panel-deep) 100%);
    display: flex;
    flex-direction: column;
  }
  .identity {
    padding: 20px 26px 18px;
    border-bottom: 1px solid var(--divider-dark);
    box-shadow: 0 1px 0 var(--divider);
  }
  .person-name {
    font-size: 25px;
    font-weight: 400;
    color: var(--text-light);
    text-transform: uppercase;
    letter-spacing: 0.3px;
    line-height: 1.1;
  }
  .person-role {
    margin-top: 6px;
    font-size: 11.5px;
    color: var(--text-muted);
    text-transform: uppercase;
    line-height: 1.3;
  }
  .contact-list { list-style: none; flex: 1; display: flex; flex-direction: column; }
  .contact-row {
    flex: 1;
    display: flex;
    align-items: center;
    gap: 18px;
    padding: 0 24px 0 26px;
    border-bottom: 1px solid var(--divider-dark);
    box-shadow: 0 1px 0 var(--divider);
  }
  .contact-row:last-child { border-bottom: none; box-shadow: none; }
  .contact-icon {
    flex: none;
    width: 44px;
    height: 44px;
    display: flex;
    align-items: center;
    justify-content: center;
  }
  .contact-icon--phone { background: var(--icon-phone); }
  .contact-icon--mail { background: var(--icon-mail); }
  .contact-icon--pin { background: var(--icon-pin); }
  .contact-text {
    font-size: 13.5px;
    color: var(--text-light);
    line-height: 1.3;
  }
  .contact-text--address { font-size: 12.5px; }
</style>
</head>
<body>
<main class="canvas">
  <article class="business-card">
    <div class="portrait" role="img" aria-label="Photograph of a woman wearing a sleek chestnut bob wig with a fringe">
      <span class="brand-name">L Radiant Tresses</span>
    </div>
    <section class="panel">
      <header class="identity">
        <h1 class="person-name">Marianne Holt</h1>
        <p class="person-role">Owner<br>Stylist Wigs/Studio</p>
      </header>
      <ul class="contact-list">
        <li class="contact-row">
          <span class="contact-icon contact-icon--phone">
            <svg width="20" height="26" viewBox="0 0 20 26" aria-hidden="true">
              <rect x="2" y="1.5" width="16" height="23" rx="2.5" fill="none" stroke="#fff" stroke-width="2"/>
              <line x1="8" y1="20.5" x2="12" y2="20.5" stroke="#fff" stroke-width="2" stroke-linecap="round"/>
            </svg>
          </span>
          <span class="contact-text">(949) 582-7041</span>
        </li>
        <li class="contact-row">
          <span class="contact-icon contact-icon--mail">
            <svg width="26" height="18" viewBox="0 0 26 18" aria-hidden="true">
              <rect x="1.5" y="1.5" width="23" height="15" fill="none" stroke="#fff" stroke-width="2"/>
              <polyline points="1.5,1.5 13,10 24.5,1.5" fill="none" stroke="#fff" stroke-width="2"/>
            </svg>
          </span>
          <span class="contact-text">wigs@lradianttresses-example.com</span>
        </li>
        <li class="contact-row">
          <span class="contact-icon contact-icon--pin">
            <svg width="20" height="26" viewBox="0 0 20 26" aria-hidden="true">
              <path d="M10 24 C10 24 2 15 2 9.5 A8 8 0 0 1 18 9.5 C18 15 10 24 10 24 Z" fill="#fff"/>
              <circle cx="10" cy="9.5" r="3.2" fill="var(--icon-pin)"/>
            </svg>
          </span>
          <span class="contact-text contact-text--address">Showroom Extensions Hair Replacement Private Room 24618 Crest Meadow Loop, Suite. R Irvine, CA 90377</span>
        </li>
      </ul>
    </section>
  </article>
</main>
</body>
</html>
```